We have over 30 years of experience in various construction projects. New additions, rehab work, interior and exterior etc. We started our own company about a year ago.
I am attaching a card that I received from a client that I really like and would like to follow as a template, but I am very open to your creative approach. I am interested in my logo (which will be later used for my website) to incorporate the "M&P" or "M&P Remodeling" Please email me at mpremodeling 81@brackenpost.com or call Rick at 773-555-0148.

Industry/Entity Type

Construction

Contact Information for Business Card

M&P Rebuild and Property Services
2816 W Ostrander Ave
Kelsford, IL 60619
708-555-0172 - Polish
708-555-0193 - English

Pawel Modrak - Owner
Edward MOdrak Jr - Construction Manager
mpremodeling81@brackenpost.com

```html
<!DOCTYPE html>
<html lang="en">
<head>
<meta charset="utf-8">
<title>M&amp;P Rebuild and Property Services – Business Cards</title>
<link href="https://fonts.googleapis.com/css2?family=Exo+2:wght@600;800&family=Saira+Condensed:wght@400;500&display=swap" rel="stylesheet">
<style>
  :root{
    --stage:#2b2630;
    --card-black:#121212;
    --card-charcoal:#2e2e2e;
    --safety-yellow:#e6e22a;
    --ink:#111111;
    --white:#f4f4f4;
    --silver:#c9c9cf;
  }
  *{box-sizing:border-box;margin:0;padding:0}
  html,body{width:1200px;height:800px;overflow:hidden;background:var(--stage)}
  .stage{position:relative;width:1200px;height:800px;display:flex;align-items:center;justify-content:center;gap:40px}
  .card{position:relative;width:540px;height:309px;overflow:hidden;border-radius:3px;box-shadow:0 14px 30px rgba(0,0,0,.45)}

  /* Front */
  .card-front{background:radial-gradient(ellipse at 70% 30%,var(--card-charcoal),var(--card-black) 75%);font-family:"Exo 2",sans-serif;color:var(--white)}
  .front-brand{position:absolute;left:30px;top:28px;display:flex;align-items:center;gap:22px}
  .brand-mark{font-weight:800;font-size:62px;line-height:1;color:var(--silver);letter-spacing:-1px}
  .brand-name{font-weight:800;font-size:27px;line-height:1.02;text-transform:uppercase;color:var(--white)}
  .people{position:absolute;left:30px;right:30px;top:140px;display:flex;align-items:flex-end;justify-content:space-between}
  .person-name{font-weight:800;font-size:17px;text-transform:uppercase;letter-spacing:.3px}
  .person-role{font-weight:600;font-size:12px;color:var(--safety-yellow);text-transform:uppercase;margin-top:2px}
  .people-divider{width:1px;height:34px;background:var(--white);opacity:.8}
  .contact-band{position:absolute;left:0;right:0;bottom:0;height:100px;background:var(--safety-yellow);color:var(--ink);padding:22px 30px 0;font-weight:600;font-size:15.5px;line-height:1.7}

  /* Back */
  .card-back{background:radial-gradient(ellipse at 50% 40%,#3a3a3a,var(--card-black) 70%);font-family:"Saira Condensed",sans-serif;color:var(--white);text-align:center}
  .back-mark{position:absolute;left:0;right:0;top:62px;font-family:"Exo 2",sans-serif;font-weight:800;font-size:96px;line-height:1;color:var(--silver)}
  .back-web{position:absolute;left:0;right:0;top:196px;font-size:18px;font-weight:500;letter-spacing:7px;text-transform:uppercase}
  .back-address{position:absolute;left:0;right:0;bottom:26px;font-size:15px;letter-spacing:1px}
</style>
</head>
<body>
<main class="stage">
  <section class="card card-front" aria-label="Business card front">
    <div class="front-brand">
      <span class="brand-mark">M&amp;P</span>
      <h1 class="brand-name">M&amp;P Rebuild and<br>Property Services</h1>
    </div>
    <div class="people">
      <div class="person left">
        <p class="person-name">English Pawel Modrak</p>
        <p class="person-role">Owner</p>
      </div>
      <span class="people-divider"></span>
      <div class="person right">
        <p class="person-name">Edward Modrak Jr</p>
        <p class="person-role">Construction Manager</p>
      </div>
    </div>
    <div class="contact-band">
      <p>Phone : 708-555-0172 &nbsp;|&nbsp; Polish : 708-555-0193</p>
      <p>Email : mpremodeling81@brackenpost.com</p>
    </div>
  </section>

  <section class="card card-back" aria-label="Business card back">
    <p class="back-mark">M&amp;P</p>
    <p class="back-web">www.mpbuildworks.us</p>
    <p class="back-address">M&amp;P Rebuild and Property Services , 2816 W Ostrander Ave Kelsford, IL 60619</p>
  </section>
</main>
</body>
</html>
```